Consulting company needs Business Cards - rough concept provided

I'm looking for someone to take our business card idea and make is slick and polished - to communicate our high-end, sophisticated, serious consulting business. We have a rough layout we did in-house. We are open to ideas on repo-ing elements, adjusting sizes, typefaces etc... within the general concept we've already come up with. We want it to be super-clean and sophisticated. We want to keep the white backgrounds, and blue brand colors. Our goal is to print with painted blue edges on thick cardstock. Thank you!!

```html
<!DOCTYPE html>
<html lang="en">
<head>
<meta charset="utf-8">
<title>Tall Thistle – Business Cards</title>
<link rel="stylesheet" href="https://fonts.googleapis.com/css2?family=Montserrat:wght@400;500;700;800&family=Raleway:wght@300&display=swap">
<style>
  :root {
    --brand-blue: #1a8fd6;
    --paper: #f4f4f2;
    --ink: #3a3a3a;
    --backdrop: #d3d7d8;
  }
  * { box-sizing: border-box; margin: 0; padding: 0; }
  html, body { width: 1200px; height: 881px; overflow: hidden; }
  body {
    background: var(--backdrop);
    font-family: "Montserrat", sans-serif;
    position: relative;
  }
  .card {
    position: absolute;
    width: 540px;
    height: 309px;
    background: var(--paper);
    border: 3px solid var(--brand-blue);
    box-shadow: 0 10px 24px rgba(0,0,0,0.18);
  }
  .card--front { left: 40px; top: 300px; }
  .card--back { left: 620px; top: 300px; }

  .wordmark {
    position: absolute;
    left: 32px;
    top: 26px;
    color: var(--brand-blue);
    font-weight: 800;
    text-transform: uppercase;
    line-height: 0.95;
    letter-spacing: -0.5px;
  }
  .wordmark__line { display: block; font-size: 50px; }
  .wordmark__line--second { padding-left: 110px; font-size: 58px; }

  .contact {
    position: absolute;
    left: 290px;
    top: 162px;
    width: 220px;
  }
  .contact__name {
    color: var(--brand-blue);
    font-weight: 700;
    font-size: 19px;
    line-height: 1.1;
  }
  .contact__title {
    color: var(--ink);
    font-size: 11px;
    font-weight: 500;
    margin-top: 3px;
  }
  .contact__rule {
    border: 0;
    border-top: 1px solid var(--brand-blue);
    margin: 8px 0 8px;
  }
  .contact__details {
    color: var(--ink);
    font-size: 11px;
    line-height: 1.45;
    font-style: normal;
  }

  .tagline {
    position: absolute;
    inset: 40px 36px;
    display: flex;
    align-items: center;
    justify-content: center;
    text-align: center;
    font-family: "Raleway", sans-serif;
    font-weight: 300;
    font-size: 19px;
    line-height: 1.55;
    color: var(--ink);
  }
  .tagline strong {
    font-family: "Montserrat", sans-serif;
    font-weight: 700;
    font-size: 24px;
    color: var(--brand-blue);
  }
</style>
</head>
<body>
  <section class="card card--front" aria-label="Business card front">
    <div class="wordmark">
      <span class="wordmark__line">Tall</span>
      <span class="wordmark__line wordmark__line--second">Thistle</span>
    </div>
    <div class="contact">
      <p class="contact__name">Dana Whitlow</p>
      <p class="contact__title">Brand Consultant</p>
      <hr class="contact__rule">
      <address class="contact__details">
        4820 Harbor Lane, Ste 210<br>
        Fairview, CA 90210<br>
        (555) 014 2290<br>
        dana@tallthistle.com
      </address>
    </div>
  </section>

  <section class="card card--back" aria-label="Business card back">
    <p class="tagline">
      <span><strong>We help</strong> [target demographic] <strong>achieve</strong> [desired emotional outcome] <strong>by</strong> [our unique approach] <strong>because</strong> [our brand beliefs]</span>
    </p>
  </section>
</body>
</html>
```